We need a business card design for our website qvwtrading.net. The Star Headline is qvwtrading.net, in large lettering.We sell fashion rings of titanium, mirror pollished stainless steel, and related jewelry. Basically quality products competing with the high expense of gold.We have to portray honesty and trust, because thats who I am. I know marketing, but I am weak on colors and layout. 3D Gold curved edge letters are ok. No green and yellow.Black,Red,Purple and White in small amounts.No fancy Lettering.
No Rainbows in printing.
Our goal is selling our products online globally

Kind Regards Maren Tulloch

Fashion

qvwtrading.net
known for our ideal fit rings
email.marentullochptyltd@corvexmail com

```html
<!DOCTYPE html>
<html lang="en">
<head>
<meta charset="utf-8">
<title>qvwtrading.net business card</title>
<link href="https://fonts.googleapis.com/css2?family=Open+Sans:wght@300&display=swap" rel="stylesheet">
<style>
  :root {
    --paper: #ffffff;
    --band: #333132;
    --gold: #a86a12;
    --bleed: #e0555f;
    --trim: #3cc0e0;
  }
  html, body {
    margin: 0;
    padding: 0;
    width: 961px;
    height: 1200px;
    overflow: hidden;
    background: var(--paper);
    font-family: "Open Sans", Arial, sans-serif;
    font-weight: 300;
  }
  .sheet { position: relative; width: 961px; height: 1200px; }
  .card {
    position: absolute;
    left: 0;
    width: 959px;
    height: 580px;
    border: 1px solid var(--bleed);
    background: var(--paper);
    overflow: hidden;
  }
  .card--front { top: 0; }
  .card--back { top: 618px; }
  .trim-line {
    position: absolute;
    left: 21px;
    top: 21px;
    width: 917px;
    height: 537px;
    border: 1px solid var(--trim);
    z-index: 3;
    pointer-events: none;
  }
  .band { position: absolute; background: var(--band); }
  .front-band { left: 0; top: 221px; width: 480px; height: 139px; }
  .hero-photo {
    position: absolute;
    left: 480px;
    top: 221px;
    width: 481px;
    height: 139px;
    background: linear-gradient(90deg, #c9c6c2 0%, #8a7a78 25%, #d8d6d8 45%, #b8b4b6 55%, #a8282a 78%, #c94040 100%);
  }
  .site-name {
    position: absolute;
    left: 85px;
    top: 266px;
    margin: 0;
    font-size: 39px;
    line-height: 1;
    font-weight: 300;
    color: var(--gold);
  }
  .tagline {
    position: absolute;
    right: 46px;
    top: 394px;
    margin: 0;
    font-size: 30px;
    line-height: 1;
    color: var(--gold);
  }
  .ring-photo {
    position: absolute;
    left: 80px;
    top: 158px;
    width: 264px;
    height: 264px;
    border-radius: 50%;
    background: radial-gradient(circle at 50% 50%, #d9a928 0%, #c8c8c8 45%, #f4f4f4 70%, #ffffff 100%);
  }
  .back-band { left: 396px; top: 174px; width: 565px; height: 230px; }
  .contact {
    position: absolute;
    left: 474px;
    top: 197px;
    margin: 0;
    font-style: normal;
    font-size: 29.5px;
    line-height: 30px;
    color: var(--gold);
  }
  .contact p { margin: 0; }
  .contact .gap { height: 30px; }
  .contact .email-address { font-size: 26px; }
</style>
</head>
<body>
<div class="sheet">
  <section class="card card--front">
    <div class="trim-line"></div>
    <div class="band front-band"></div>
    <h1 class="site-name">www.qvwtrading.net</h1>
    <div class="hero-photo" role="img" aria-label="Close-up photo of a polished chrome wheel with red machinery behind"></div>
    <p class="tagline">Known for our ideal fit rings</p>
  </section>

  <section class="card card--back">
    <div class="trim-line"></div>
    <div class="ring-photo" role="img" aria-label="Product photo of a gold and silver titanium ring with screw details"></div>
    <div class="band back-band"></div>
    <address class="contact">
      <p>Email</p>
      <p class="email-address">marentullochptyltd@corvexmail.com</p>
      <div class="gap"></div>
      <p>Fax</p>
      <p>+61 02 5550 1834 (International)</p>
      <p>02 5550 1834 (Local)</p>
    </address>
  </section>
</div>
</body>
</html>
```